Bref créative
Real Estate Development Firm
Marlow Holdings
I need double sided standard sized Business Card [3.5" x 2"]
May use same font as in logo or other suggestions
Professional
Derek P. Hollins
President/CEO
248 West Penrose Street
Suite 2360
Milwaukee, WI 53217
dhollins@marlowholdingsllc.example
marlowholdingsllc.example
You can refer to logo design contest for other ideas.
Logo and design or color gradient or other suggestions.
Please use logo

```html
<!DOCTYPE html>
<html lang="en">
<head>
<meta charset="utf-8">
<title>Marlow Holdings – Business Card</title>
<link rel="stylesheet" href="https://fonts.googleapis.com/css2?family=Source+Sans+3:wght@400;600;700&display=swap">
<style>
  :root {
    --page: #ffffff;
    --blue-light: #5b83ea;
    --blue-mid: #3a5bd6;
    --blue-deep: #1d2c99;
    --gray-light: #f4f4f4;
    --gray-mid: #c9c9c9;
    --ink-dark: #2b2f6b;
    --white: #ffffff;
    --edge: #0b0b14;
  }
  * { margin: 0; padding: 0; box-sizing: border-box; }
  html, body { width: 1200px; height: 904px; overflow: hidden; background: var(--page); }
  body { position: relative; font-family: "Source Sans 3", sans-serif; }

  .card { position: absolute; left: 382px; width: 460px; height: 265px; overflow: hidden; }
  .card-front { top: 192px; }
  .card-back {
    top: 467px;
    background: linear-gradient(180deg, var(--blue-light) 0%, var(--blue-mid) 55%, var(--blue-deep) 100%);
  }
  .front-art { position: absolute; inset: 0; }

  .brand {
    position: absolute; left: 28px; top: 116px; width: 180px;
    display: flex; align-items: center; gap: 7px;
  }
  .brand-mark { width: 12px; height: 12px; background: var(--blue-mid); flex: none; }
  .brand-name { font-size: 17px; font-weight: 600; color: var(--ink-dark); letter-spacing: 0.3px; white-space: nowrap; }

  .contact { position: absolute; right: 18px; top: 36px; text-align: right; color: var(--white); }
  .contact-name { font-size: 17px; font-weight: 700; line-height: 1; }
  .contact-title { font-size: 9px; margin-top: 4px; }
  .contact-address { font-size: 10px; line-height: 15px; margin-top: 44px; }
  .contact-phones { margin-top: 20px; font-size: 10px; line-height: 17px; display: grid; grid-template-columns: 22px 72px; justify-content: end; text-align: left; }
  .phone-label { font-weight: 700; }
  .contact-email { font-size: 10px; margin-top: 19px; }

  .back-brand {
    position: absolute; left: 0; right: 0; top: 96px;
    display: flex; justify-content: center; align-items: center; gap: 9px;
  }
  .back-mark { width: 14px; height: 14px; background: var(--white); }
  .back-name { font-size: 22px; font-weight: 600; color: var(--white); letter-spacing: 0.4px; }
  .back-web { position: absolute; left: 170px; top: 200px; font-size: 9px; color: var(--white); }
</style>
</head>
<body>
  <section class="card card-front">
    <svg class="front-art" width="460" height="265" viewBox="0 0 460 265">
      <defs>
        <linearGradient id="front-gray" x1="0" y1="0" x2="1" y2="1">
          <stop offset="0" stop-color="var(--gray-light)"/>
          <stop offset="1" stop-color="var(--gray-mid)"/>
        </linearGradient>
        <linearGradient id="front-blue" x1="0" y1="0" x2="0" y2="1">
          <stop offset="0" stop-color="var(--blue-light)"/>
          <stop offset="0.55" stop-color="var(--blue-mid)"/>
          <stop offset="1" stop-color="var(--blue-deep)"/>
        </linearGradient>
      </defs>
      <rect width="460" height="265" fill="url(#front-gray)"/>
      <path d="M108 0 Q 262 132 108 265 L 460 265 L 460 0 Z" fill="var(--edge)"/>
      <path d="M122 0 Q 272 132 122 265 L 460 265 L 460 0 Z" fill="url(#front-blue)"/>
    </svg>

    <div class="brand">
      <span class="brand-mark"></span>
      <span class="brand-name">Marlow Holdings</span>
    </div>

    <div class="contact">
      <p class="contact-name">Derek P. Hollins</p>
      <p class="contact-title">President/CEO</p>
      <p class="contact-address">248 West Penrose Street<br>Suite 2360, Milwaukee, WI 53217</p>
      <div class="contact-phones">
        <span class="phone-label">P :</span><span>414.555.0142</span>
        <span class="phone-label">C :</span><span>414.555.0187</span>
        <span class="phone-label">F :</span><span>414.555.0193</span>
      </div>
      <p class="contact-email">dhollins@marlowholdingsllc.example</p>
    </div>
  </section>

  <section class="card card-back">
    <div class="back-brand">
      <span class="back-mark"></span>
      <span class="back-name">Marlow Holdings</span>
    </div>
    <p class="back-web">www.marlowholdingsllc.example</p>
  </section>
</body>
</html>
```